Ward Compass Business Card Design*

We need a business card design for our company Ward Compass. Our company is specialized in providing online consulting services regarding medical institutions, hospitals and doctors. We work with patients worldwide looking to choose between healthcare providers. We have a website you may use as a reference, where we list doctors and clinics worldwide. So we target Medical providers as well as patients worldwide.
Target Market(s)
Medical Providers and patients around the world
Industry/Entity Type
Medical
Contact Information for Business Card
Salma Derkaoui
CEO
+90 612 348 2071
info@wardcompass-example.com
www.wardcompass-example.com
14 Annakhil 3 H.R.B. Rabat, Morocco
Requirements
Must have
- Company logo/name on one full side, personal info and smaller logo and company name on the other side.
Nice to have
- Smart and elegant design

```html
<!DOCTYPE html>
<html lang="en">
<head>
<meta charset="utf-8">
<title>Ward Compass Business Card</title>
<link href="https://fonts.googleapis.com/css2?family=Montserrat:wght@400;500;600;700&display=swap" rel="stylesheet">
<style>
  :root {
    --stage: #878787;
    --card: #ffffff;
    --navy: #1d3562;
    --grey-text: #7b7b7b;
    --white: #ffffff;
  }
  * { margin: 0; padding: 0; box-sizing: border-box; }
  html, body { width: 1200px; height: 1000px; overflow: hidden; }
  body {
    background: var(--stage);
    font-family: "Montserrat", Arial, sans-serif;
    position: relative;
  }
  .card {
    position: absolute;
    left: 216px;
    width: 770px;
    height: 440px;
    background: var(--card);
    box-shadow: 0 2px 8px rgba(0,0,0,0.35);
    overflow: hidden;
  }
  .card--front { top: 41px; }
  .card--back { top: 516px; }

  .brand {
    position: absolute;
    display: flex;
    align-items: center;
    color: var(--navy);
    font-weight: 700;
    white-space: nowrap;
  }
  .brand__dot {
    border-radius: 50%;
    background: var(--navy);
    flex: none;
  }
  .brand--large {
    left: 0; right: 0; top: 160px;
    justify-content: center;
    font-size: 40px;
    letter-spacing: 1px;
    gap: 20px;
  }
  .brand--large .brand__dot { width: 60px; height: 60px; }
  .brand--small {
    left: 448px; top: 72px;
    font-size: 22px;
    letter-spacing: 0.5px;
    gap: 12px;
  }
  .brand--small .brand__dot { width: 38px; height: 38px; }

  .web-band {
    position: absolute;
    background: var(--navy);
    color: var(--white);
    display: flex;
    align-items: center;
    justify-content: center;
    text-align: center;
    white-space: nowrap;
    font-weight: 600;
  }
  .card--front .web-band {
    left: 0; right: 0; bottom: 0; height: 55px;
    font-size: 15px;
    letter-spacing: 3px;
  }
  .card--back .web-band {
    left: 421px; width: 320px; bottom: 0; height: 56px;
    font-size: 11.5px;
    letter-spacing: 1.6px;
  }

  .name-band {
    position: absolute;
    left: 0; top: 48px;
    width: 421px; height: 104px;
    background: var(--navy);
    color: var(--white);
    padding: 24px 0 0 42px;
  }
  .name-band__name {
    font-size: 33px;
    font-weight: 500;
    letter-spacing: 0.5px;
    line-height: 1;
    white-space: nowrap;
  }
  .name-band__role {
    font-size: 17px;
    letter-spacing: 6px;
    margin-top: 10px;
    font-weight: 500;
  }
  .edge-tab {
    position: absolute;
    left: 740px; top: 48px;
    width: 30px; height: 104px;
    background: var(--navy);
  }

  .contact-list {
    position: absolute;
    left: 41px; top: 180px;
    list-style: none;
  }
  .contact-list::before {
    content: "";
    position: absolute;
    left: 17px; top: 20px;
    width: 2px; height: 100px;
    background: var(--navy);
  }
  .contact-list__item {
    position: relative;
    display: flex;
    align-items: center;
    height: 34px;
    margin-bottom: 15px;
    color: var(--grey-text);
    font-size: 20px;
    font-weight: 500;
    white-space: nowrap;
  }
  .contact-list__icon {
    width: 35px; height: 35px;
    border-radius: 50%;
    background: var(--navy);
    display: flex; align-items: center; justify-content: center;
    margin-right: 10px;
    flex: none;
  }
</style>
</head>
<body>

<section class="card card--front">
  <div class="brand brand--large"><span class="brand__dot"></span>WARD COMPASS</div>
  <div class="web-band">WWW.WARDCOMPASS-EXAMPLE.COM</div>
</section>

<section class="card card--back">
  <div class="name-band">
    <div class="name-band__name">SALMA DERKAOUI</div>
    <div class="name-band__role">CEO</div>
  </div>
  <div class="brand brand--small"><span class="brand__dot"></span>WARD COMPASS</div>
  <div class="edge-tab"></div>

  <ul class="contact-list">
    <li class="contact-list__item">
      <span class="contact-list__icon">
        <svg width="20" height="20" viewBox="0 0 24 24" aria-hidden="true">
          <path d="M6.6 10.8a15 15 0 0 0 6.6 6.6l2.2-2.2c.3-.3.7-.4 1-.2 1.1.4 2.3.6 3.6.6.6 0 1 .4 1 1V20c0 .6-.4 1-1 1A17 17 0 0 1 3 4c0-.6.4-1 1-1h3.5c.6 0 1 .4 1 1 0 1.3.2 2.5.6 3.6.1.3 0 .7-.2 1z" fill="#fff"/>
        </svg>
      </span>
      +90 612 348 2071
    </li>
    <li class="contact-list__item">
      <span class="contact-list__icon">
        <svg width="22" height="22" viewBox="0 0 24 24" aria-hidden="true">
          <text x="12" y="18" text-anchor="middle" font-family="Arial, sans-serif" font-size="20" font-weight="700" fill="#fff">@</text>
        </svg>
      </span>
      INFO@WARDCOMPASS-EXAMPLE.COM
    </li>
    <li class="contact-list__item">
      <span class="contact-list__icon">
        <svg width="22" height="22" viewBox="0 0 24 24" aria-hidden="true" fill="none" stroke="#fff" stroke-width="1.4">
          <circle cx="12" cy="12" r="9"/>
          <ellipse cx="12" cy="12" rx="4" ry="9"/>
          <line x1="3" y1="12" x2="21" y2="12"/>
          <line x1="5" y1="7" x2="19" y2="7"/>
          <line x1="5" y1="17" x2="19" y2="17"/>
        </svg>
      </span>
      WWW.WARDCOMPASS-EXAMPLE.COM
    </li>
  </ul>

  <div class="web-band">WWW.WARDCOMPASS-EXAMPLE.COM</div>
</section>

</body>
</html>
```